Vehicle Signage Design for a Renovation Company

We're a renovation company specialising in Home Renovations. The final design should communicate trust, credibility, and confidence. We need vehicle signage designed for our company utes (see attachment) / for our grey ute with the canopy/ and white use withou the canopyI've also attached our existing designs for the current vehicles (van and hatch back) to give you an idea of what we're after.In terms of content, there isn't much requirement for this due to the limited space on the ute - but happy to hear ideas on this.We've tried designing it ourselves - see attachment, but not happy with the result, would like more variations and ideas.Check out our website www.kestrelrenovations.co.nz for ideas on our branding/ style.
Updates

Target Market(s)

Home Owners

Industry/Entity Type

Residential Construction

Font styles to use
Sans Serif

Colors
3276b5
0355a3
33a6d7
3aa7d7
ffffff

Requirements
Must have
• Logo, Call to Action (website and number), Headline
Nice to have
• Strong sharp lines, a clean/sleek look
• It would be nice to have our offer on there (free design plans) / but we know space is limited

```html
<!DOCTYPE html>
<html lang="en">
<head>
<meta charset="utf-8">
<title>Kestrel Home Renovations – Ute Signage</title>
<link rel="stylesheet" href="https://fonts.googleapis.com/css2?family=Rubik:wght@400;500;700&family=Caveat:wght@500&display=swap">
<style>
  :root {
    --canvas-navy: #1c1566;
    --body-white: #ffffff;
    --band-blue: #283f94;
    --band-edge: #3276b5;
    --band-deep: #1f2f7a;
    --panel-charcoal: #2a2f3a;
    --brand-blue: #2b3f98;
    --ink-black: #111111;
    --cut-line: #c0303a;
  }
  html, body {
    margin: 0;
    padding: 0;
    width: 1200px;
    height: 885px;
    overflow: hidden;
    background: var(--canvas-navy);
  }
  .ute-artwork { display: block; width: 1200px; height: 885px; }
  .ute-body { fill: var(--body-white); stroke: var(--cut-line); stroke-width: 1.2; }
  .band-main { fill: var(--band-blue); }
  .band-edge { fill: var(--band-edge); }
  .band-deep { fill: var(--band-deep); }
  .panel-lower { fill: var(--panel-charcoal); }
  .brand-name { font-family: "Rubik", sans-serif; font-weight: 700; font-size: 86px; fill: var(--brand-blue); }
  .brand-tag { font-family: "Rubik", sans-serif; font-weight: 700; font-size: 20px; fill: var(--ink-black); }
  .headline { font-family: "Rubik", sans-serif; font-weight: 500; font-size: 23px; fill: var(--body-white); }
  .offer { font-family: "Rubik", sans-serif; font-weight: 400; font-size: 13px; fill: var(--body-white); }
  .consult { font-family: "Rubik", sans-serif; font-weight: 400; font-size: 12.5px; fill: var(--body-white); }
  .phone { font-family: "Rubik", sans-serif; font-weight: 500; font-size: 22px; fill: var(--body-white); }
  .website { font-family: "Rubik", sans-serif; font-weight: 400; font-size: 10.5px; fill: var(--body-white); }
  .call-script { font-family: "Caveat", cursive; font-weight: 500; font-size: 16px; fill: var(--body-white); }
  .trust-line { font-family: "Rubik", sans-serif; font-weight: 500; font-size: 12px; fill: var(--body-white); }
</style>
</head>
<body>
<svg class="ute-artwork" viewBox="0 0 1200 885" xmlns="http://www.w3.org/2000/svg" aria-label="Kestrel Home Renovations ute side wrap layout">
  <defs>
    <clipPath id="ute-outline">
      <path clip-rule="evenodd" d="M70,866 L64,838 L66,812 L96,808 L98,792 L70,788 L66,760 L72,738 L112,732 L122,712 L170,697 L280,682 L405,673 L440,640 L515,580 L830,568 Q862,568 866,592 L874,683 L1196,683 Q1212,684 1212,700 L1214,760 L1220,800 L1190,818 L1084,868 A100 100 0 0 0 886,880 L882,895 L370,898 A106 106 0 0 0 162,868 Z M412,692 L498,598 L655,588 L658,696 Z M680,586 L812,586 Q822,586 824,596 L832,690 L680,694 Z"/>
    </clipPath>
  </defs>

  <g class="ute-layout" transform="translate(-23,-269) scale(0.97)">
    <path class="ute-body" fill-rule="evenodd" d="M70,866 L64,838 L66,812 L96,808 L98,792 L70,788 L66,760 L72,738 L112,732 L122,712 L170,697 L280,682 L405,673 L440,640 L515,580 L830,568 Q862,568 866,592 L874,683 L1196,683 Q1212,684 1212,700 L1214,760 L1220,800 L1190,818 L1084,868 A100 100 0 0 0 886,880 L882,895 L370,898 A106 106 0 0 0 162,868 Z M412,692 L498,598 L655,588 L658,696 Z M680,586 L812,586 Q822,586 824,596 L832,690 L680,694 Z"/>

    <g class="wrap-graphics" clip-path="url(#ute-outline)">
      <polygon class="band-edge" points="350,878 880,732 1230,674 1230,684 880,740 350,888"/>
      <polygon class="band-main" points="350,886 880,738 1230,682 1230,760 885,806 540,910 350,910"/>
      <polygon class="band-deep" points="530,900 885,796 1230,750 1230,760 885,806 545,910"/>
      <polygon class="panel-lower" points="540,910 885,804 1230,758 1230,930 540,930"/>
    </g>

    <text class="brand-name" transform="translate(358,822) rotate(-17)">Kestrel</text>
    <text class="brand-tag" transform="translate(545,800) rotate(-15)">HOME RENOVATIONS</text>

    <g class="headline-block" transform="translate(505,860) rotate(-15.5)">
      <text class="headline" x="0" y="0">THINKING ABOUT RENOVATING</text>
      <text class="headline" x="0" y="25">YOUR HOME?</text>
      <text class="offer" x="150" y="15">Get your free design plans</text>
      <text class="offer" x="154" y="29">(worth $2,500)</text>
    </g>

    <g class="consult-block" transform="translate(878,752) rotate(-8)">
      <text class="consult" x="0" y="0">Book a free design</text>
      <text class="consult" x="-2" y="14">to build consultation</text>
    </g>

    <g class="contact-block" transform="translate(1012,733) rotate(-4)">
      <text class="phone" x="0" y="0">0800 555 014</text>
      <text class="website" x="2" y="13">www.kestrelrenovations.co.nz</text>
    </g>

    <g class="call-to-action" transform="translate(1092,792) rotate(-20)">
      <text class="call-script" x="0" y="0">secure your</text>
      <text class="call-script" x="4" y="15">spot now</text>
    </g>

    <g class="trust-block" transform="translate(765,850)">
      <text class="trust-line" x="0" y="0">TRUSTED HOME</text>
      <text class="trust-line" x="0" y="15">RENOVATION</text>
      <text class="trust-line" x="0" y="30">EXPERTS</text>
    </g>
  </g>
</svg>
</body>
</html>
```